Everett's Book Cover

Need a cover design for a book (paperback and eBook)
Book Title: Where The Cedar Rivers Bend
Book Width: 15.24
Book Height: 22.86
Thickness: approximately 200 pages.
Book is a collection of stories drawn from the author's life, and will be in the local history genre in northern British Columbia, Canada from the period 1930 to the present time.
Author: Everett Hollis Pelletier
Must include "As told to Marnie Kowal" on front cover, not on the spine.
Author invites designers creativity and asks that the attached photos be incorporated into the front and back covers in tasteful ways as follows:
Other uses of the photos will be considered.
We apologize for the quality of the photos. Please do what you can.
We look forward to your designs.
Thank you for considering.

Target Market(s)

Lovers of local history, jokes, storytelling, back country hiking and mountain climbing. Men and women 30 years and older. Primary target readership are men and women in their 40's, 50's, 60's, and older, who love local history

Font styles to use
Sans Serif

Requirements
Must have
• Back cover copy must clear and easy to read.
Must appeal to outdoor, back country types.
Nice to have
• Like to see a creative incorporation of the photos provided.
Build on or compliment the colours in the photos

```html
<!DOCTYPE html>
<html lang="en">
<head>
<meta charset="utf-8">
<title>Where The Cedar Rivers Bend — Front Cover</title>
<link rel="stylesheet" href="https://fonts.googleapis.com/css2?family=Cinzel:wght@400&family=EB+Garamond:ital@1&family=Archivo:wght@500&display=swap">
<style>
  :root {
    --backdrop: #1c2222;
    --title-ink: #262628;
    --byline-ink: #1c1c1c;
    --sky-top: #8b8fbd;
    --sky-mid: #aeb3d2;
    --cloud: #eef0f5;
    --ridge: #8d8986;
    --snow: #e8e6e3;
    --forest: #5f6a3e;
    --meadow-far: #b89c42;
    --meadow: #a98e38;
    --meadow-near: #8a7f3a;
    --foliage: #6f7640;
    --mist: #f2f0ea;
  }
  html, body {
    margin: 0;
    width: 1200px;
    height: 1166px;
    overflow: hidden;
    background: var(--backdrop);
  }
  .cover {
    position: absolute;
    left: 270px;
    top: 88px;
    width: 660px;
    height: 990px;
    overflow: hidden;
    box-shadow: 0 24px 60px rgba(0, 0, 0, 0.55);
  }
  .cover-photo {
    position: absolute;
    inset: 0;
    background:
      radial-gradient(ellipse 70% 12% at 50% 100%, var(--mist) 0%, rgba(242, 240, 234, 0) 100%),
      radial-gradient(ellipse 45% 18% at 30% 84%, rgba(111, 118, 64, 0.75) 0%, rgba(111, 118, 64, 0) 100%),
      radial-gradient(ellipse 40% 16% at 78% 80%, rgba(196, 164, 72, 0.7) 0%, rgba(196, 164, 72, 0) 100%),
      radial-gradient(ellipse 55% 10% at 62% 45%, rgba(232, 230, 227, 0.85) 0%, rgba(232, 230, 227, 0) 100%),
      radial-gradient(ellipse 30% 6% at 88% 50%, rgba(95, 106, 62, 0.7) 0%, rgba(95, 106, 62, 0) 100%),
      radial-gradient(ellipse 60% 14% at 35% 28%, rgba(238, 240, 245, 0.95) 0%, rgba(238, 240, 245, 0) 100%),
      radial-gradient(ellipse 50% 10% at 80% 12%, rgba(238, 240, 245, 0.8) 0%, rgba(238, 240, 245, 0) 100%),
      linear-gradient(
        to bottom,
        var(--sky-top) 0%,
        var(--sky-mid) 14%,
        #d4d6e6 30%,
        #b8bbd3 38%,
        #a19fa8 42%,
        #b9b6b2 46%,
        #8f8c78 50%,
        var(--meadow-far) 55%,
        var(--meadow) 66%,
        var(--meadow-near) 78%,
        #a49c6c 88%,
        #d8d4c2 95%,
        var(--mist) 100%
      );
  }
  .title {
    position: absolute;
    left: 0;
    right: 0;
    top: 56px;
    margin: 0;
    text-align: center;
    font-family: "Cinzel", serif;
    font-weight: 400;
    color: var(--title-ink);
    line-height: 1;
  }
  .title-line { display: block; }
  .title-line--large { font-size: 74px; }
  .title-line--small { font-size: 36px; margin: 6px 0 8px; }
  .title-line--wide { font-size: 62px; margin-bottom: 8px; }
  .credit {
    position: absolute;
    left: 0;
    right: 0;
    top: 884px;
    margin: 0;
    text-align: center;
    font-family: "EB Garamond", serif;
    font-style: italic;
    font-size: 24px;
    color: var(--byline-ink);
  }
  .author {
    position: absolute;
    left: 0;
    right: 0;
    top: 928px;
    margin: 0;
    text-align: center;
    font-family: "Archivo", sans-serif;
    font-weight: 500;
    font-size: 24px;
    letter-spacing: 2.5px;
    color: var(--byline-ink);
  }
</style>
</head>
<body>
  <main class="cover">
    <div class="cover-photo" role="img" aria-label="Photograph of a hiker with a backpack and rifle walking through a meadow of yellow wildflowers below a snow-patched mountain peak under a cloudy blue sky"></div>
    <h1 class="title">
      <span class="title-line title-line--large">WHERE</span>
      <span class="title-line title-line--small">THE</span>
      <span class="title-line title-line--wide">CEDAR RIVERS</span>
      <span class="title-line title-line--large">BEND</span>
    </h1>
    <p class="credit">"As told to Marnie Kowal"</p>
    <p class="author">EVERETT HOLLIS PELLETIER</p>
  </main>
</body>
</html>
```